Food Label Packaging Design Remake Redesign

We are ready for a redo! We want to remake our food label to be more fun, beachy and modern to better reflect our brand's desired vibe and the actual meaning of ‘hullabaloo’ as a boisterous party, noisy excitement.

Please first reference the current label and logo elements attached. You can also reference our website www.hullabalooqsmoke.com. We want to give our current look the refreshed look described above.

The remaining images represent a design board of interest and inspiration for new color combinations, font style, background, cowgirl meets beach and surf!

REQUIRED elements are
1) The full company name: HULLABALOO BBQ spelled like this and all caps.
2) The cowgirl - she can be modified to include the surfboard somehow to make her a beachy cowgirl/maybe surfer girl - but she cannot be in a bikini she needs to still have pants/boots on...as in a 'mash up' of cowgirl and beach/surfer girl that represents the noisy excitement of a 'hullabaloo' . Please do NOT cut her in half
3) The ‘Tucked with a Hug’ seal to have that matches to have a beachy, playful feel to it, maybe palm tree/kiss lips combo ?
4) Much of the right side of the label must be included but can be presented in a totally different way: the preparation directions, the nutritional panel nd bottom right product information. all can be rearranged - its most important that the preparation instructions are legible.
5) Product title

**Please DO NOT make country-western**

Target Market(s)

Moms, Dads and Singles who are 'foodies' with a busy family and social, work schedule who value authentic, great tasting food that is authentic, boutique and better than for you, convenient, and fun to feed and entertain their friends and families.

Industry/Entity Type

food - CPG Consumer Packaged Foods

Font styles to use
Other font styles liked:
• Cursive, playful andf fun! PLEASE SEE FONT IDEAS IN IMAGES ATTACHED

Colors
0094D4
00A9DD
6FCCEA
C7EBF8
E9F6FB
00AB8E
00BBA5
67D7C9
C6EFE9
E9F9F6
FFC000
F8CF3A
FAE287
FDF2CF
FEFAEE
F0912C
F2A743
F7CA91
FBE8D2
FDF5EE
E54698
E96AAD
F1A4CE
F9D9EA
FCEFF6

Requirements
Must have
• Please see above. Colors: I would like to maintain pink as the main color, along with a cool new beachy black/gray. The other colors below are of interest and are also represented in image ideas provided. Logo - take out 'Marlena's BBQ' and include the phonetic description of hullabaloo near/a part of logo hullabaloo: /hul uh buh loo/ Ingredients and Nutrtional panel - content doesn't have to be exact but must be represented to scale, but may be decreased in size, especially the nutrition panel. Please be sure the preparation instructions are legible, not too small.
Nice to have
• PLEASE SEE THE NEW INFO GRAPHIC with the 'sun' to consider and also the fun, cursive font to consider in your design. thank you!
Should not have
• Please see above!

```html
<!DOCTYPE html>
<html lang="en">
<head>
<meta charset="utf-8">
<title>Hullabaloo BBQ – Smoked Chopped Label</title>
<link rel="stylesheet" href="https://fonts.googleapis.com/css2?family=Oswald:wght@500;700&family=Montserrat:wght@500;700;800&family=Roboto+Condensed:wght@400;700&family=Libre+Franklin:wght@400;700;900&display=swap">
<style>
  :root {
    --backdrop: #ece4d6;
    --ink: #2a1a22;
    --pink-sky: #f3a3cb;
    --pink-glow: #fbe3ef;
    --title-pink: #de5f7c;
    --title-shade: #b8425f;
    --sea-deep: #0f7f8c;
    --sea: #1aa3ad;
    --sand: #f1dcae;
    --sand-light: #f8ead0;
    --alert-red: #e4202a;
    --white: #ffffff;
    --black: #0c0c0c;
  }
  * { box-sizing: border-box; margin: 0; padding: 0; }
  html, body { width: 1200px; height: 900px; overflow: hidden; }
  body { background: var(--backdrop); position: relative; }

  .label {
    position: absolute; left: 30px; top: 68px;
    width: 1140px; height: 763px;
    display: flex; background: var(--white);
    box-shadow: 0 14px 26px rgba(0,0,0,.22);
    overflow: hidden;
  }

  /* front panel */
  .front { position: relative; width: 703px; height: 100%; color: var(--ink); }
  .front__scene {
    position: absolute; inset: 0;
    background:
      radial-gradient(ellipse 320px 260px at 50% 42%, var(--pink-glow) 0%, rgba(251,227,239,0) 100%),
      linear-gradient(to bottom,
        var(--pink-sky) 0%, #f6bcd9 58%, #f4b3d4 63%,
        var(--sea-deep) 63%, var(--sea) 72%, #1c9aa6 78%,
        var(--sand) 79%, var(--sand-light) 100%);
  }
  .front__rider {
    position: absolute; left: 424px; top: 12px; width: 112px; height: 80px;
    border-radius: 10px;
    background: linear-gradient(135deg, #4a3040 0%, #6b4a5a 100%);
    opacity: .35;
  }
  .front__brand {
    position: absolute; top: 100px; left: 0; width: 100%;
    text-align: center;
    font: 700 62px/1 "Oswald", sans-serif; letter-spacing: 1px;
    color: var(--ink);
  }
  .front__tagline {
    position: absolute; top: 178px; left: 0; width: 100%;
    text-align: center;
    font: 700 15px/1 "Montserrat", sans-serif; letter-spacing: 3px;
  }
  .front__title {
    position: absolute; left: 0; width: 100%; text-align: center;
    font: 700 112px/1 "Oswald", sans-serif; color: var(--title-pink);
    text-shadow: 3px 3px 0 var(--title-shade);
  }
  .front__title--one { top: 200px; }
  .front__title--two { top: 314px; }
  .front__subtitle {
    position: absolute; top: 432px; left: 0; width: 100%; text-align: center;
    font: 500 26px/1 "Montserrat", sans-serif; letter-spacing: 4px;
  }
  .front__storage {
    position: absolute; top: 695px; left: 0; width: 100%; text-align: center;
    font: 800 19px/25px "Montserrat", sans-serif; letter-spacing: 1px;
  }

  /* back panel */
  .back { position: relative; flex: 1; height: 100%; }
  .directions {
    position: absolute; left: 15px; top: 17px; width: 174px; height: 730px;
    overflow: hidden;
    font: 400 16.5px/24.5px "Roboto Condensed", sans-serif; color: var(--ink);
  }
  .directions strong { font-weight: 700; }
  .directions__alert { color: var(--alert-red); font-weight: 700; text-transform: uppercase; margin-bottom: 20px; }
  .directions__block { margin-bottom: 20px; }
  .directions__heading { font-weight: 700; text-transform: uppercase; }
  .directions__ingredients { font-weight: 700; }

  .nutrition {
    position: absolute; left: 199px; top: 11px; width: 223px;
    border: 1.5px solid var(--black); padding: 2px 4px 3px;
    font: 400 9.5px/13px "Libre Franklin", sans-serif; color: var(--black);
  }
  .nutrition__title { font: 900 25px/26px "Libre Franklin", sans-serif; }
  .nutrition__serving { display: flex; justify-content: space-between; font-weight: 700; font-size: 10.5px; border-bottom: 6px solid var(--black); padding-bottom: 1px; }
  .nutrition__amount { font-weight: 700; font-size: 8.5px; margin-top: 2px; }
  .nutrition__calories { display: flex; justify-content: space-between; font: 900 20px/22px "Libre Franklin", sans-serif; border-bottom: 4px solid var(--black); }
  .nutrition__dv { text-align: right; font-size: 6.5px; border-bottom: 1px solid var(--black); }
  .nutrition__row { display: flex; justify-content: space-between; border-bottom: 1px solid var(--black); height: 14px; }
  .nutrition__row b { font-weight: 700; }
  .nutrition__row--indent { padding-left: 10px; }
  .nutrition__row--indent2 { padding-left: 22px; }
  .nutrition__row--thick { border-bottom-width: 6px; height: 18px; }
  .nutrition__row--caffeine { font-weight: 700; font-size: 11px; height: 18px; border-bottom-width: 3px; }
  .nutrition__note { font-size: 6px; line-height: 8px; padding-top: 2px; }

  .distributor {
    position: absolute; left: 199px; top: 400px; width: 223px; height: 126px;
    background: var(--black); color: var(--white);
    font: 400 12.5px/17.5px "Roboto Condensed", sans-serif;
    padding: 21px 0 0 14px;
  }
  .distributor strong { font-weight: 700; }
  .distributor__badge {
    position: absolute; right: 10px; top: 20px; width: 88px; height: 88px;
    border-radius: 50%; background: var(--white);
  }

  .social {
    position: absolute; right: 18px; top: 538px; text-align: right;
    font: 700 16.5px/24px "Roboto Condensed", sans-serif; color: var(--title-pink);
  }
  .seal { position: absolute; left: 242px; top: 588px; }
</style>
</head>
<body>
  <div class="label">
    <section class="front">
      <div class="front__scene" role="img" aria-label="Beach scene illustration: pink sky, palm trees on both sides, teal ocean waves, sandy shore with a pink and a yellow striped surfboard"></div>
      <div class="front__rider" role="img" aria-label="Cowgirl in hat, pants and boots riding a surfboard on a wave"></div>
      <div class="front__brand">HULLABALOO BBQ</div>
      <div class="front__tagline">/hul uh buh loo/</div>
      <div class="front__title front__title--one">SMOKED</div>
      <div class="front__title front__title--two">CHOPPED</div>
      <div class="front__subtitle">BEEF BRISKET BBQ</div>
      <div class="front__storage">KEEP FROZEN / REFRIGERATED<br>NET WT. 16OZ(1LB)</div>
    </section>

    <section class="back">
      <div class="directions">
        <p class="directions__alert">Fully cooked!<br>Just heat, serve, and enjoy!</p>
        <p class="directions__heading">Reheat instructions:</p>
        <p class="directions__block"><strong>OVEN:</strong> Lorem ipsum dolor sit amet, consectetuer adipiscing elit, sed diam nonummy nibh euismod tincidunt ut laoreet dolore magna aliquam erat volutpat.</p>
        <p class="directions__block"><strong>MICROWAVE:</strong> Lorem ipsum dolor sit amet, consectetuer adipiscing elit, sed diam nonummy nibh euismod tincidunt ut laoreet dolore magna aliquam erat volutpat.</p>
        <p class="directions__ingredients">INGREDIENTS: Ut wisi enim ad minim veniam, quis nostrud exerci tation ullamcorper suscipit lobortis nisl ut Lorem ipsum dolor sit amet, consec-</p>
      </div>

      <div class="nutrition">
        <div class="nutrition__title">Nutrition Facts</div>
        <div>1 serving per container</div>
        <div class="nutrition__serving"><span>Serving size &nbsp;8 oz.</span><span>(236ml)</span></div>
        <div class="nutrition__amount">Amount per serving</div>
        <div class="nutrition__calories"><span>Calories</span><span>181</span></div>
        <div class="nutrition__dv">% Daily Value*</div>
        <div class="nutrition__row"><span><b>Total Fat</b> 7.5g</span><b>12%</b></div>
        <div class="nutrition__row nutrition__row--indent"><span>Saturated Fat 4.3g</span><b>21%</b></div>
        <div class="nutrition__row nutrition__row--indent"><span><i>Trans</i> fat 0.3g</span><span></span></div>
        <div class="nutrition__row"><span><b>Cholesterol</b> 23mg</span><b>8%</b></div>
        <div class="nutrition__row"><span><b>Sodium</b> 150mg</span><b>6%</b></div>
        <div class="nutrition__row"><span><b>Total Carbohydrate</b> 21g</span><b>7%</b></div>
        <div class="nutrition__row nutrition__row--indent"><span>Dietary fiber 0.1g</span><b>0.2%</b></div>
        <div class="nutrition__row nutrition__row--indent"><span>Total sugars 19g</span><span></span></div>
        <div class="nutrition__row nutrition__row--indent2"><span>Includes 7g Added Sugars</span><b>14%</b></div>
        <div class="nutrition__row nutrition__row--thick"><span><b>Protein</b> 7.8g</span><span></span></div>
        <div class="nutrition__row"><span>Vit D 2.6mcg</span><b>27%</b></div>
        <div class="nutrition__row"><span>Calcium 273mg</span><b>27%</b></div>
        <div class="nutrition__row"><span>Iron 0.1mg</span><b>0.6%</b></div>
        <div class="nutrition__row nutrition__row--thick"><span>Potassium 347mg</span><b>10%</b></div>
        <div class="nutrition__row nutrition__row--caffeine"><span>Caffeine</span><span>13.5mg</span></div>
        <p class="nutrition__note">* The % Daily Value (DV) tells you how much of a nutrient in a serving of food contributes to a daily diet. 2,000 calories a day is used for general nutrition advice.</p>
      </div>

      <div class="distributor">
        <p>DISTRIBUTED BY:<br><strong>HULLABALOO BBQ</strong><br>418 Tidewater Lane<br>Coral Bay,<br>VA 23999</p>
        <div class="distributor__badge" role="img" aria-label="Inspection badge"></div>
      </div>

      <div class="social">#HULLABALOOLIVIN<br>WWW.HULLABALOOQSMOKE.COM</div>

      <svg class="seal" width="152" height="152" viewBox="0 0 152 152" role="img" aria-label="Tucked with a Hug seal">
        <circle cx="76" cy="76" r="74" fill="#de5f7c"/>
      </svg>
    </section>
  </div>
</body>
</html>
```